Online Course Page

We are building a video based online course page. This project is for only the actual page that the student will watch the videos at. They will watch one vide at a time. Once one video lesson is completed then they can move to the next video lesson. The page will need to show the video player. (Main feature.) The list of lessons in the course. Instructor information. Profile picture and bio of the instructor. A Live chat button that will initiate a chat in real-time with the instructor.

The winning designer will also be asked to to design the dashboard area and other aspects of the user interface as an additional project.

Target Market(s)

Adults

Number of Pages Required

1 page

Colors
9bcb3c

Requirements
Must have
• Our logo is attached. Green and grey are our colors. Should feel modern, clean and be simple to navigate. The site will be responsive so the layout should work well on mobile devices.

```html
<!DOCTYPE html>
<html lang="en">
<head>
<meta charset="utf-8">
<title>CSS Grid Layout – LearnGrove</title>
<link href="https://fonts.googleapis.com/css2?family=Roboto:wght@400;500;700&display=swap" rel="stylesheet">
<style>
  :root {
    --green: #9bcb3c;
    --page-bg: #f4f4f4;
    --white: #ffffff;
    --text-dark: #3d3d3d;
    --text-body: #5a5a5a;
    --link-blue: #3f6fa8;
    --line: #e2e2e2;
    --panel-bg: #efefef;
    --video-dark: #0a1a4a;
    --video-deep: #050f33;
    --control-bg: #0b1233;
    --track: #6a6a6a;
  }
  * { box-sizing: border-box; margin: 0; padding: 0; }
  html, body { width: 893px; height: 1200px; overflow: hidden; }
  body {
    position: relative;
    background: var(--page-bg);
    font-family: "Roboto", Arial, sans-serif;
    color: var(--text-dark);
  }

  /* Header */
  .site-header {
    position: absolute; left: 0; top: 0; width: 893px; height: 55px;
    background: var(--white); border-bottom: 1px solid var(--line);
  }
  .brand {
    position: absolute; left: 55px; top: 14px;
    display: flex; align-items: center; gap: 7px;
    font-size: 17px; font-weight: 700; color: var(--text-dark);
  }
  .brand-dot { width: 22px; height: 22px; border-radius: 50%; background: var(--green); }
  .search {
    position: absolute; left: 189px; top: 12px; width: 246px; height: 28px;
    background: var(--page-bg); border-radius: 3px;
    font-size: 11px; color: #a0a0a0; padding: 8px 13px;
  }
  .search svg { position: absolute; right: 13px; top: 7px; }
  .nav-item {
    position: absolute; top: 20px; font-size: 11.5px; color: var(--text-dark);
    display: flex; align-items: center; gap: 4px;
  }
  .account { position: absolute; left: 797px; top: 14px; display: flex; align-items: center; gap: 5px; }
  .account-avatar { width: 28px; height: 28px; border-radius: 50%; background: #e3e3e3; }

  /* Title */
  .course-title {
    position: absolute; left: 55px; top: 76px;
    font-size: 22px; font-weight: 500; color: var(--text-dark);
  }

  /* Player */
  .player {
    position: absolute; left: 55px; top: 130px; width: 782px; height: 482px;
    background: var(--white); box-shadow: 0 1px 3px rgba(0,0,0,.12);
  }
  .video-frame {
    position: absolute; left: 0; top: 0; width: 782px; height: 440px;
    background: radial-gradient(ellipse at 40% 35%, #13328c 0%, var(--video-dark) 55%, var(--video-deep) 100%);
  }
  .controls {
    position: absolute; left: 0; top: 413px; width: 782px; height: 27px;
    background: rgba(5, 10, 35, .85);
  }
  .progress { position: absolute; left: 20px; top: 1px; width: 741px; height: 3px; background: var(--track); }
  .progress-fill { width: 261px; height: 3px; background: var(--green); }
  .play-btn { position: absolute; left: 27px; top: 8px; }
  .timecode { position: absolute; left: 63px; top: 9px; font-size: 10.5px; color: var(--white); }
  .fullscreen-btn { position: absolute; right: 28px; top: 7px; }
  .next-lesson {
    position: absolute; right: 13px; top: 470px;
    font-size: 11.5px; font-weight: 500; color: var(--green);
    display: flex; align-items: center; gap: 4px;
  }
  .player .next-lesson { top: 456px; }

  /* About card */
  .about-card {
    position: absolute; left: 55px; top: 635px; width: 783px; height: 514px;
    background: #f8f8f8; box-shadow: 0 1px 3px rgba(0,0,0,.12);
  }
  .about-title { position: absolute; left: 13px; top: 18px; font-size: 16px; font-weight: 500; }
  .about-text {
    position: absolute; left: 13px; top: 44px; width: 490px;
    font-size: 11px; line-height: 18px; color: var(--text-body);
  }

  .module {
    position: absolute; left: 13px; width: 487px; height: 41px;
    background: var(--green); color: var(--white); border-radius: 2px;
    font-size: 15.5px; font-weight: 500; padding: 10px 13px;
    display: flex; align-items: center; gap: 10px;
  }
  .lesson-list {
    position: absolute; left: 13px; top: 169px; width: 487px;
    background: var(--white); border: 1px solid var(--line); border-top: 0; list-style: none;
  }
  .lesson {
    position: relative; height: 34.4px; border-bottom: 1px solid var(--line);
    font-size: 11px; color: var(--link-blue); padding: 11px 13px;
  }
  .lesson:last-child { border-bottom: 0; }
  .lesson.is-hover { background: #f6f6f6; }
  .lesson-time { position: absolute; left: 409px; top: 11px; color: var(--text-body); }
  .lesson-play { position: absolute; left: 455px; top: 8px; }

  /* Instructor */
  .instructor {
    position: absolute; left: 536px; top: 46px; width: 233px; height: 328px;
    background: var(--panel-bg);
  }
  .instructor-heading { position: absolute; left: 12px; top: 13px; font-size: 12.5px; font-weight: 500; }
  .instructor-photo {
    position: absolute; left: 12px; top: 40px; width: 86px; height: 86px; border-radius: 50%;
    background: radial-gradient(circle at 50% 45%, #b08a74 0%, #5a4236 55%, #2e3f58 100%);
  }
  .instructor-name { position: absolute; left: 118px; top: 53px; font-size: 11.5px; color: var(--text-body); }
  .live-chat {
    position: absolute; left: 118px; top: 78px; width: 98px; height: 27px;
    background: var(--green); color: var(--white); border-radius: 2px;
    font-size: 11px; font-weight: 500; display: flex; align-items: center; justify-content: center; gap: 6px;
  }
  .instructor-bio {
    position: absolute; left: 12px; top: 154px; width: 218px;
    font-size: 10.8px; line-height: 13.6px; color: var(--text-body);
  }
  .show-more {
    position: absolute; left: 12px; top: 276px; font-size: 11px; font-weight: 500; color: var(--text-dark);
    display: flex; align-items: center; gap: 3px;
  }
</style>
</head>
<body>

<header class="site-header">
  <div class="brand"><span class="brand-dot"></span>LearnGrove</div>
  <div class="search">Search for courses
    <svg width="12" height="12" viewBox="0 0 12 12"><circle cx="5" cy="5" r="3.8" fill="none" stroke="#9bcb3c" stroke-width="1.6"/><line x1="7.8" y1="7.8" x2="11" y2="11" stroke="#9bcb3c" stroke-width="1.8"/></svg>
  </div>
  <div class="nav-item" style="left:457px">Courses
    <svg width="8" height="5" viewBox="0 0 8 5"><path d="M1 1l3 3 3-3" fill="none" stroke="#3d3d3d"/></svg>
  </div>
  <div class="nav-item" style="left:529px">Categories
    <svg width="8" height="5" viewBox="0 0 8 5"><path d="M1 1l3 3 3-3" fill="none" stroke="#3d3d3d"/></svg>
  </div>
  <div class="account">
    <div class="account-avatar"></div>
    <svg width="8" height="5" viewBox="0 0 8 5"><path d="M1 1l3 3 3-3" fill="none" stroke="#3d3d3d"/></svg>
  </div>
</header>

<h1 class="course-title">CSS Grid Layout</h1>

<section class="player">
  <div class="video-frame" role="img" aria-label="Video lesson still: close-up of CSS code on a dark blue screen"></div>
  <div class="controls">
    <div class="progress"><div class="progress-fill"></div></div>
    <svg class="play-btn" width="9" height="12" viewBox="0 0 9 12"><path d="M0 0l9 6-9 6z" fill="#fff"/></svg>
    <span class="timecode">1:34/4:44</span>
    <svg class="fullscreen-btn" width="14" height="13" viewBox="0 0 14 13" fill="none" stroke="#fff" stroke-width="1.3"><path d="M1 4V1h3M10 1h3v3M13 9v3h-3M4 12H1V9"/><rect x="4" y="4" width="6" height="5"/></svg>
  </div>
  <a class="next-lesson">Next Lesson
    <svg width="5" height="8" viewBox="0 0 5 8"><path d="M1 1l3 3-3 3" fill="none" stroke="#9bcb3c" stroke-width="1.3"/></svg>
  </a>
</section>

<section class="about-card">
  <h2 class="about-title">About the course.</h2>
  <p class="about-text">Lorem ipsum dolor sit amet, consectetur adipiscing elit. In aliquam nisi vel elit consectetur vehicula. In enim tellus, efficitur at tristique vehicula, gravida vitae sem. Morbi eu pulvinar lectus. Curabitur quam odio, vehicula varius luctus ut, mattis nec purus.</p>

  <div class="module" style="top:128px">Introducing Grid Layout
    <svg width="11" height="7" viewBox="0 0 11 7"><path d="M1 1l4.5 4.5L10 1" fill="none" stroke="#fff" stroke-width="1.5"/></svg>
  </div>
  <ul class="lesson-list">
    <li class="lesson">Understanding Grid<span class="lesson-time">3:21</span>
      <svg class="lesson-play" width="18" height="18" viewBox="0 0 18 18"><circle cx="9" cy="9" r="8" fill="none" stroke="#b5b5b5"/><path d="M7 5.5l5 3.5-5 3.5z" fill="#b5b5b5"/></svg></li>
    <li class="lesson is-hover">Grid Concepts and Terminology<span class="lesson-time">2:31</span>
      <svg class="lesson-play" width="18" height="18" viewBox="0 0 18 18"><circle cx="9" cy="9" r="8" fill="none" stroke="#b5b5b5"/><path d="M7 5.5l5 3.5-5 3.5z" fill="#b5b5b5"/></svg></li>
    <li class="lesson">Defining a Gid<span class="lesson-time">4:55</span>
      <svg class="lesson-play" width="18" height="18" viewBox="0 0 18 18"><circle cx="9" cy="9" r="8" fill="none" stroke="#b5b5b5"/><path d="M7 5.5l5 3.5-5 3.5z" fill="#b5b5b5"/></svg></li>
    <li class="lesson">Setting Grid Rows<span class="lesson-time">5:23</span>
      <svg class="lesson-play" width="18" height="18" viewBox="0 0 18 18"><circle cx="9" cy="9" r="8" fill="none" stroke="#b5b5b5"/><path d="M7 5.5l5 3.5-5 3.5z" fill="#b5b5b5"/></svg></li>
    <li class="lesson">Add Gutters Between Rows and Columns<span class="lesson-time">4:33</span>
      <svg class="lesson-play" width="18" height="18" viewBox="0 0 18 18"><circle cx="9" cy="9" r="8" fill="none" stroke="#b5b5b5"/><path d="M7 5.5l5 3.5-5 3.5z" fill="#b5b5b5"/></svg></li>
  </ul>

  <div class="module" style="top:363px">Flexible Sized Grids
    <svg width="7" height="11" viewBox="0 0 7 11"><path d="M1 1l4.5 4.5L1 10" fill="none" stroke="#fff" stroke-width="1.5"/></svg>
  </div>
  <div class="module" style="top:418px">List of Lessons in an Accordion
    <svg width="7" height="11" viewBox="0 0 7 11"><path d="M1 1l4.5 4.5L1 10" fill="none" stroke="#fff" stroke-width="1.5"/></svg>
  </div>

  <aside class="instructor">
    <h3 class="instructor-heading">Instructor</h3>
    <div class="instructor-photo" role="img" aria-label="Portrait photo of the instructor"></div>
    <div class="instructor-name">Daniel Moreau</div>
    <a class="live-chat">
      <svg width="16" height="13" viewBox="0 0 16 13"><path d="M1.5 1.5h13v8H6l-3 2.5v-2.5H1.5z" fill="none" stroke="#fff" stroke-width="1.3" stroke-linejoin="round"/></svg>
      Live Chat
    </a>
    <p class="instructor-bio">Lorem ipsum dolor sit amet, consectetur adipiscing elit. In aliquam nisi vel elit consectetur vehicula. In enim tellus, efficitur at tristique vehicula, gravida vitae sem. Morbi eu pulvinar lectus. Curabitur quam odio, vehicula varius luctus ut, mattis nec purus. Nam elementum nibh vel nisl fermentum rhoncus.</p>
    <a class="show-more">Show More
      <svg width="5" height="8" viewBox="0 0 5 8"><path d="M1 1l3 3-3 3" fill="none" stroke="#3d3d3d" stroke-width="1.3"/></svg>
    </a>
  </aside>
</section>

</body>
</html>
```